Flyer-Design für Kosmetiker-Netzwerk gesucht
Das war eine ganz hervorragende Zusammenarbeit. Wiebke war stets offen für alle Anregungen und Sonderwünsche meinerseits, ergänzte diese durch kreative Vorschläge ihrerseits. In jedem ihrer Vorschläge war Fachkompetenz ersichtlich und durch ihre freundliches und offenes Wesen konnte diese Aufgabe schnell zu einem exzellenten Abschluss gebracht werden. Ich freue mich auf weitere Projekte und wünsche ihr auf der Plattform von grafikhafen.de stetigen Erfolg.
Zielgruppe
Unserer Service: Wir bieten die Erstellung eines großen Netzwerkes aus unabhängig arbeitender Kosmetikstudios - für eine starke Gemeinschaft mit hoher Marketingleistung.
Zielgruppe: Das Design sollte für Betreiber/innen von Kosmetikstudios so gestaltet sein, daß es dahin überzeugend wirkt - sich dem Netzwerk anzuschließen und um gemeinsam mehr zu erreichen.
Aufgabenstellung
Erstellt werden soll ein 8-seitiger Flyer im 3-Bruch Fensterfalz. Das Format kann DIN sein, muss aber nicht. Bitte benutzt CMYK-Farben und keine Sonderfarben. Die folgenden Ideen können als Anreiz gesehen werden, welche aber nicht verpflichtend sind: Alle 4 Innenseiten 7-8 Fotos von Kosmetikerinnen/Studios/Behandlungen/... - siehe Anhang...alle Fotos können beigestellt werden
- ebenfalls auf den 4 Innenseiten - 12 Aussagen mit den Vorteilen als Mitglied des Netzwerkes auffällig und einprägend gestaltet (Texte werden in Nachhinein beigestellt) - für die Gestaltung 'Lorem ipsum...'
- 2 Innenseiten (nach einmaligen Aufklappen)...Foto mit Suchmaschine, Logo und weltumspannendes Netzwerk
- Vorder- und Rückseite (vollständig zusammengeklappt)...Vorderseite: Logo auf neutralem Hintergrund - Rückseite: QR-Code und E-Mail-Adresse
- Schriftart: Century Gothic
Bei Rückfragen bitte melden...

```html
<!DOCTYPE html>
<html lang="de">
<head>
<meta charset="utf-8">
<title>Kosmo Verbund – Flyer Fensterfalz</title>
<link href="https://fonts.googleapis.com/css2?family=Questrial&family=Open+Sans:wght@400;600&display=swap" rel="stylesheet">
<style>
:root{
  --stage:#cfcfcf;
  --gap:#ffffff;
  --paper:#fbfbfb;
  --panel-grey:#ececec;
  --ink:#3a3a3a;
  --ink-soft:#6a6a6a;
  --accent:#b8292a;
  --night:#1e1f22;
  --night-mid:#4a4d55;
}
*{box-sizing:border-box;margin:0;padding:0}
html,body{width:1200px;height:3245px;overflow:hidden;background:var(--gap)}
.stage{position:absolute;left:0;width:1200px;height:800px;background:var(--stage);display:flex;align-items:center;justify-content:center;gap:0}
.stage--cover{top:0}
.stage--outer{top:815px}
.stage--window{top:1630px}
.stage--inner{top:2445px}
.sheet{display:flex;box-shadow:0 18px 30px rgba(0,0,0,.18)}
.panel{position:relative;background:var(--paper);overflow:hidden;font-family:"Open Sans",sans-serif;color:var(--ink)}
.panel + .panel{border-left:1px solid #dcdcdc}
.panel--tall{width:300px;height:640px}
.panel--mid{width:260px;height:560px}
.panel--inner{width:270px;height:580px}
.accent-band{position:absolute;left:0;right:0;bottom:0;height:14px;background:var(--accent)}
.photo{position:absolute;left:0;right:0}
.brand{font-family:"Questrial",sans-serif;color:var(--ink);letter-spacing:.12em;text-transform:uppercase;line-height:1.05}
.cover .brand{position:absolute;top:42px;left:0;right:0;text-align:center;font-size:38px}
.cover .photo{top:170px;bottom:14px;background:linear-gradient(180deg,#f7f7f7 0%,#ece6e2 55%,#dcc8c0 100%)}
.cover .claim{position:absolute;right:22px;bottom:42px;text-align:right;font-family:"Questrial",sans-serif;font-size:19px;letter-spacing:.08em;line-height:1.25;color:var(--ink);text-transform:uppercase}
.network{background:var(--night)}
.network .photo{top:0;bottom:0;background:radial-gradient(circle at 55% 38%,#8b8f98 0%,var(--night-mid) 35%,var(--night) 75%)}
.network .title{position:absolute;right:22px;font-family:"Questrial",sans-serif;color:#fff;font-size:22px;letter-spacing:.1em;text-align:right;line-height:1.2;text-transform:uppercase}
.network .copy{position:absolute;left:22px;right:22px;font-size:10.5px;line-height:1.5;color:#e8e8e8;text-align:right}
.panel--mid.network .title{bottom:120px}
.panel--mid.network .copy{bottom:32px}
.panel--tall.network .title{bottom:150px}
.panel--tall.network .copy{bottom:44px;font-size:12px}
.contact .brand{position:absolute;top:28px;left:24px;font-size:13px}
.contact h2{position:absolute;top:90px;left:24px;font-family:"Questrial",sans-serif;font-weight:400;font-size:18px;letter-spacing:.08em;line-height:1.2}
.contact .copy{position:absolute;top:150px;left:24px;right:24px;font-size:9.5px;line-height:1.5;color:var(--ink-soft)}
.contact address{position:absolute;top:210px;left:24px;right:24px;font-style:normal;font-size:9.5px;line-height:1.5;color:var(--ink-soft)}
.contact .photo{top:330px;bottom:0;background:linear-gradient(180deg,var(--paper) 0%,#e9e6e3 60%,#c9c4bf 100%)}
.benefits .photo--top{top:0;height:150px}
.benefits h3{position:absolute;top:170px;left:20px;right:16px;font-family:"Questrial",sans-serif;font-weight:400;font-size:17px;letter-spacing:.08em;text-transform:uppercase}
.benefits ol{position:absolute;top:210px;left:20px;right:18px;list-style:none;counter-reset:item}
.benefits li{counter-increment:item;position:relative;padding-left:22px;margin-bottom:12px;font-size:9.5px;line-height:1.45;color:var(--ink-soft)}
.benefits li::before{content:counter(item);position:absolute;left:0;top:-3px;font-family:"Questrial",sans-serif;font-size:18px;color:var(--ink)}
.benefits .photo--bottom{left:34px;right:34px;bottom:48px;height:110px}
.benefits .brand{position:absolute;top:22px;left:18px;font-size:12px;z-index:1}
.benefits .band-grey{position:absolute;left:0;right:0;top:150px;height:360px;background:var(--panel-grey)}
</style>
</head>
<body>

<section class="stage stage--cover" aria-label="Titelseite und Rückseite">
  <div class="sheet">
    <article class="panel panel--tall cover">
      <div class="brand">Kosmo<br>Verbund</div>
      <div class="photo" role="img" aria-label="Porträtfoto einer Frau mit futuristischer Brille auf hellem Grund"></div>
      <p class="claim">Das Netzwerk<br>für die Kosmetik<br>Branche</p>
      <div class="accent-band"></div>
    </article>
    <article class="panel panel--tall benefits">
      <div class="photo photo--top" role="img" aria-label="Foto lachender Frauen, von oben fotografiert" style="background:linear-gradient(135deg,#e8d6cc,#b88f7f)"></div>
      <div class="band-grey"></div>
      <h3>Ihr Mehrwert</h3>
      <ol>
        <li>Neue Kundinnen finden Sie über unser gemeinsames Online-Verzeichnis.</li>
        <li>Professionelle Vorlagen für Flyer, Anzeigen und Social Media stehen bereit.</li>
        <li>Gemeinsame Aktionstage bringen spürbar mehr Besucherinnen in Ihr Studio.</li>
      </ol>
      <div class="photo photo--bottom" role="img" aria-label="Foto einer Massage mit Handtüchern" style="background:linear-gradient(135deg,#f0e2d4,#c89a7a)"></div>
      <div class="accent-band"></div>
    </article>
  </div>
</section>

<section class="stage stage--outer" aria-label="Außenseite aufgeklappt">
  <div class="sheet">
    <article class="panel panel--mid network">
      <div class="photo" role="img" aria-label="Foto einer Hand vor einem leuchtenden, weltumspannenden Netzwerk"></div>
      <h2 class="title">Wer<br>wir sind</h2>
      <p class="copy">Wir verbinden unabhängige Studios zu einem starken Netzwerk mit gemeinsamer Marketingkraft und vielen Vorteilen für jedes Mitglied vor Ort.</p>
    </article>
    <article class="panel panel--mid contact">
      <div class="brand">Kosmo Verbund</div>
      <h2>Lorem ipsum<br>dolor</h2>
      <p class="copy">Gemeinsam erreichen wir mehr Sichtbarkeit, neue Kundinnen und bessere Konditionen für Ihr Studio.</p>
      <address>Kosmo Verbund<br>Lindenweg 8<br>20457 Hafenstadt<br>Tel. +49 (0)40 555 2210<br>Fax +49 (0)40 555 2211<br>info@kosmo-verbund.de<br>www.kosmo-verbund.de</address>
      <div class="photo" role="img" aria-label="Foto gestapelter Massagesteine auf einer Hand"></div>
    </article>
    <article class="panel panel--mid cover">
      <div class="brand" style="font-size:30px">Kosmo<br>Verbund</div>
      <div class="photo" style="top:140px" role="img" aria-label="Porträtfoto einer Frau mit futuristischer Brille auf hellem Grund"></div>
      <p class="claim" style="font-size:16px">Das Netzwerk<br>für die Kosmetik<br>Branche</p>
      <div class="accent-band"></div>
    </article>
    <article class="panel panel--mid network">
      <div class="photo" role="img" aria-label="Foto eines leuchtenden Netzwerks aus verbundenen Punkten"></div>
    </article>
  </div>
</section>

<section class="stage stage--window" aria-label="Innenseite nach dem ersten Aufklappen">
  <div class="sheet">
    <article class="panel panel--tall network">
      <div class="photo" role="img" aria-label="Linke Hälfte eines Fotos mit weltumspannendem Netzwerk"></div>
    </article>
    <article class="panel panel--tall network">
      <div class="photo" role="img" aria-label="Rechte Hälfte eines Fotos mit weltumspannendem Netzwerk und Hand"></div>
      <h2 class="title">Wer<br>wir sind</h2>
      <p class="copy">Wir verbinden unabhängige Studios zu einem starken Netzwerk mit gemeinsamer Marketingkraft und vielen Vorteilen für jedes Mitglied vor Ort.</p>
    </article>
  </div>
</section>

<section class="stage stage--inner" aria-label="Innenseiten vollständig aufgeklappt">
  <div class="sheet">
    <article class="panel panel--inner benefits">
      <div class="brand">Kosmo Verbund</div>
      <div class="photo photo--top" role="img" aria-label="Foto umgekippter Nagellackfläschchen" style="background:linear-gradient(180deg,var(--paper) 30%,#c85a7a)"></div>
      <div class="band-grey"></div>
      <h3>3 gute Gründe</h3>
      <ol>
        <li>Gemeinsame Werbeaktionen machen Ihr Studio in der ganzen Region sichtbar und bekannt.</li>
        <li>Bessere Einkaufskonditionen bei Herstellern senken Ihre laufenden Kosten deutlich.</li>
        <li>Regelmäßiger Austausch mit Kolleginnen bringt neue Ideen in Ihren Alltag.</li>
      </ol>
      <div class="photo photo--bottom" role="img" aria-label="Foto einer Kosmetikerin in ihrem Studio" style="background:linear-gradient(135deg,#f4f2ef,#c9bfb5)"></div>
      <div class="accent-band"></div>
    </article>
    <article class="panel panel--inner benefits">
      <div class="photo photo--top" role="img" aria-label="Nahaufnahme eines geschminkten Auges" style="background:linear-gradient(135deg,#f2e9e2,#b99b86)"></div>
      <h3>Ihre Vorteile</h3>
      <ol>
        <li>Eine starke Marke steht hinter Ihnen und schafft Vertrauen bei Kundinnen.</li>
        <li>Sie bleiben selbstständig und entscheiden weiterhin frei über Ihr Angebot.</li>
        <li>Schulungen und Workshops halten Ihr Team fachlich stets auf dem neuesten Stand.</li>
      </ol>
      <div class="photo photo--bottom" role="img" aria-label="Foto einer Gesichtsbehandlung" style="background:linear-gradient(135deg,#efe6df,#b59382)"></div>
      <div class="accent-band"></div>
    </article>
    <article class="panel panel--inner benefits">
      <div class="photo photo--top" role="img" aria-label="Foto lachender Frauen, von oben fotografiert" style="background:linear-gradient(135deg,#e8d6cc,#b88f7f)"></div>
      <div class="band-grey"></div>
      <h3>Ihr Mehrwert</h3>
      <ol>
        <li>Neue Kundinnen finden Sie über unser gemeinsames Online-Verzeichnis.</li>
        <li>Professionelle Vorlagen für Flyer, Anzeigen und Social Media stehen bereit.</li>
        <li>Gemeinsame Aktionstage bringen spürbar mehr Besucherinnen in Ihr Studio.</li>
      </ol>
      <div class="photo photo--bottom" role="img" aria-label="Foto einer Massage mit Handtüchern" style="background:linear-gradient(135deg,#f0e2d4,#c89a7a)"></div>
      <div class="accent-band"></div>
    </article>
    <article class="panel panel--inner benefits">
      <div class="photo photo--top" role="img" aria-label="Foto einer Rückenbehandlung mit Peeling" style="background:linear-gradient(135deg,#efe3da,#8c6a58)"></div>
      <h3>Ihr Gewinn</h3>
      <ol>
        <li>Mehr Zeit für Behandlungen, weil wir Marketing für Sie übernehmen.</li>
        <li>Ein starkes Netzwerk gibt Sicherheit und Rückhalt in jeder Saison.</li>
        <li>Ihr Erfolg wächst mit jedem neuen Mitglied der Gemeinschaft.</li>
      </ol>
      <div class="photo photo--bottom" role="img" aria-label="Foto einer Frau mit Gesichtsmaske" style="background:linear-gradient(135deg,#f6f3f0,#cfc3b8)"></div>
      <div class="accent-band"></div>
    </article>
  </div>
</section>

</body>
</html>
```